We need a design for a contracting company website based in KSA, something modern with the same color theme as the attached logo. including a page for people who want to submit their CV and try to apply for a job.Also to include the "about us, contact us, gallery, Divisions, Supplies, etc...". If possible to have an interactive or moving background. Please disregard the "Keen Methods" Section in the attached profile.

Industry/Entity Type

Construction Company

Number of Pages Required

5+ page

Colors

Designer to choose colors to be used in the design.

Requirements
Must have
• Pages:
• about us, contact us, gallery, Divisions, Apply for a job, Supplies
Nice to have
• - Moving or interactive background

```html
<!DOCTYPE html>
<html lang="en">
<head>
<meta charset="utf-8">
<title>Cobaltrine Building Company</title>
<link rel="stylesheet" href="https://fonts.googleapis.com/css2?family=Montserrat:ital,wght@0,400;0,500;0,600;0,700;1,400&display=swap">
<style>
:root{
  --gold:#f6a823;
  --gold-deep:#e8951a;
  --ink:#1d1d1d;
  --text:#555;
  --muted:#888;
  --line:#ddd;
  --white:#fff;
  --dark:#262523;
}
*{margin:0;padding:0;box-sizing:border-box}
html,body{width:1200px;height:4240px;overflow:hidden}
body{font-family:'Montserrat',sans-serif;color:var(--ink);background:var(--white);position:relative}
.abs{position:absolute}
section,header,footer,nav.footer-nav{position:absolute;left:0;width:1200px}

/* top bar */
.topbar{top:0;left:0;width:1200px;height:36px;background:var(--gold);color:var(--white);font-size:11px;z-index:3}
.topbar .phone{left:172px;top:11px;display:flex;align-items:center;gap:6px}
.topbar .socials{right:172px;top:7px;display:flex;gap:14px}
.topbar .socials span{width:22px;height:22px;border-radius:50%;background:var(--ink);display:block}

/* header */
.site-header{top:36px;height:137px;background:var(--white);border-bottom:1px solid #eee}
.brand{left:160px;top:44px;display:flex;align-items:center;gap:8px;font-weight:700;font-size:17px;color:var(--gold);letter-spacing:.5px}
.brand i{width:14px;height:14px;background:var(--gold);display:block}
.apply-btn{left:903px;top:32px;width:125px;height:36px;border-radius:6px;background:var(--gold);color:var(--white);font-size:10px;font-weight:600;display:flex;align-items:center;justify-content:center;box-shadow:0 2px 4px rgba(0,0,0,.2)}
.main-nav{top:88px;left:450px;font-size:13px;font-weight:500}
.main-nav a{color:var(--ink);text-decoration:none;position:absolute;top:0;white-space:nowrap}

/* hero */
.hero{top:173px;height:568px}
.hero .photo{position:absolute;inset:0;background:linear-gradient(100deg,#2c2a27 0%,#6d5a3e 25%,#b48f5b 45%,#8a7b6a 65%,#3b3d52 85%,#2a2520 100%)}
.hero .welcome{left:0;top:175px;width:100%;text-align:center;color:var(--white);font-size:22px;font-weight:500}
.hero h1{left:0;top:207px;width:100%;text-align:center;color:var(--white);font-size:35px;font-weight:700;line-height:46px}
.hero h1 em{font-style:normal;color:var(--gold)}
.hero .btn{top:309px;width:124px;height:36px;border-radius:4px;font-size:10px;font-weight:700;color:var(--white);display:flex;align-items:center;justify-content:center}
.hero .btn.learn{left:465px;background:var(--gold);box-shadow:0 3px 6px rgba(0,0,0,.4)}
.hero .btn.contact{left:613px;border:2px solid var(--white)}
.hero .arrow{top:270px;width:32px;height:32px;background:var(--white);display:flex;align-items:center;justify-content:center}

/* about */
.about{top:741px;height:400px}
.about .portrait{left:187px;top:51px;width:300px;height:300px;border-radius:50%;border:6px solid var(--gold);background:linear-gradient(160deg,#d9c8a4,#8c8f8a 60%,#3a3a3a)}
.about h2{left:543px;top:92px;font-size:27px;font-weight:600}
.about .rule{left:540px;top:137px;width:28px;height:2px;background:var(--gold)}
.about p{left:540px;top:155px;width:490px;font-size:11px;line-height:19px;color:var(--muted)}
.about .read{left:538px;top:268px;width:124px;height:36px;border-radius:4px;background:var(--gold);color:var(--white);font-size:10px;font-weight:700;display:flex;align-items:center;justify-content:center}
.about .years{left:688px;top:268px;width:84px;height:89px;border:3px solid var(--gold);border-radius:4px;font-size:48px;font-weight:700;display:flex;align-items:center;justify-content:center}
.about .years-label{left:786px;top:298px;font-size:13px;font-weight:600;line-height:16px}

/* divisions */
.divisions{top:1155px;height:262px}
.division{top:0;width:365px;height:261px;border-radius:4px;overflow:hidden;color:var(--white);text-align:center}
.division .img{position:absolute;inset:0}
.division h3{position:absolute;left:0;top:148px;width:100%;font-size:18px;font-weight:700}
.division p{position:absolute;top:180px;left:35px;right:35px;font-size:11px;line-height:20px}

/* services */
.services{top:1460px;height:520px}
.section-title{left:0;width:100%;text-align:center;font-size:26px;font-weight:600}
.title-rule{left:585px;width:30px;height:2px;background:var(--gold)}
.services .worker{left:478px;top:125px;width:246px;height:395px;border-radius:120px 120px 0 0;background:linear-gradient(180deg,#f2c14a 0%,#d9a88a 25%,#2b3560 55%,#1e2649 100%)}
.svc{width:320px}
.svc h4{font-size:17px;font-weight:700;letter-spacing:.3px}
.svc p{margin-top:27px;font-size:11px;line-height:20px;color:var(--muted)}
.svc.left{left:128px;text-align:right}
.svc.right{left:759px}

/* stats */
.stats{top:1978px;height:184px;background:var(--gold);border-top:5px solid var(--ink);border-bottom:5px solid var(--ink)}
.stat{top:0;width:200px;height:174px;text-align:center;color:var(--ink)}
.stat svg{position:absolute;left:85px;top:28px}
.stat b{position:absolute;left:0;top:78px;width:200px;font-size:30px;font-weight:600}
.stat span{position:absolute;left:0;top:135px;width:200px;font-size:12px;font-weight:700;color:var(--white);letter-spacing:.4px}

/* testimonials */
.testimonials{top:2200px;height:557px}
.avatar{border-radius:50%;background:linear-gradient(160deg,#bbb,#666);border:3px solid var(--white);box-shadow:0 3px 10px rgba(0,0,0,.25)}
.testimonials .quote{left:250px;top:252px;width:700px;text-align:center;font-size:12px;font-style:italic;line-height:22px;color:var(--text)}
.testimonials .name{left:0;top:318px;width:100%;text-align:center;font-size:12px;font-weight:700}
.testimonials .role{left:0;top:338px;width:100%;text-align:center;font-size:10px;font-style:italic;color:var(--text)}
.dots{top:490px;left:574px;display:flex;gap:8px}
.dots i{width:11px;height:11px;border-radius:50%;border:2px solid var(--ink);display:block}
.dots i.on{border-color:var(--gold)}

/* why */
.why{top:2757px;height:565px;overflow:hidden}
.why .photo{position:absolute;inset:0;background:linear-gradient(120deg,#c98a3a 0%,#7d6f60 25%,#3b3a38 50%,#6a4a2c 78%,#f07a1e 100%)}
.why .disc{left:436px;top:-353px;width:872px;height:872px;border-radius:50%;background:rgba(24,24,24,.9)}
.why h2{left:662px;top:121px;font-size:27px;font-weight:600;color:var(--white)}
.why .rule{left:662px;top:167px;width:30px;height:2px;background:var(--white)}
.why p{left:662px;top:185px;width:382px;font-size:11px;line-height:19.5px;color:var(--white)}
.why .btn{left:663px;top:401px;width:125px;height:36px;border-radius:4px;background:var(--white);color:var(--gold);font-size:10px;font-weight:700;display:flex;align-items:center;justify-content:center}

/* contact */
.contact{top:3322px;height:390px}
.contact h2{left:245px;top:83px;font-size:27px;font-weight:600}
.contact .rule{left:245px;top:124px;width:28px;height:2px;background:var(--gold)}
.contact .help{left:245px;top:148px;font-size:12px;color:var(--text);letter-spacing:.3px}
.contact .big-phone{left:244px;top:172px;font-size:34px;font-weight:600;color:var(--gold)}
.contact .addr{left:245px;top:232px;font-size:12px;color:var(--text)}
.contact .mail{left:245px;top:270px;font-size:12px;font-weight:600;color:var(--gold)}
.field{left:611px;width:344px;border:1px solid var(--line);border-radius:3px;font-size:10px;color:#999;padding:12px 18px;box-shadow:0 1px 4px rgba(0,0,0,.08)}
.field svg{position:absolute;right:12px;top:11px}
.submit{left:611px;top:302px;width:344px;height:37px;border-radius:4px;background:linear-gradient(90deg,var(--gold) 0%,#d89a2a 55%,#2a2520 100%);color:var(--white);font-size:11px;font-weight:700;display:flex;align-items:center;justify-content:center}

/* footer nav & subscribe */
.footer-nav{top:3727px;height:30px;font-size:13px;font-weight:500}
.footer-nav a{position:absolute;top:0;color:var(--ink);text-decoration:none}
.site-footer{top:3829px;height:411px}
.site-footer .photo{position:absolute;left:0;top:0;width:1200px;height:360px;background:linear-gradient(110deg,#4a4d2a 0%,#3a3a33 35%,#2e2d2b 60%,#4a3e2b 100%)}
.site-footer .photo::after{content:"";position:absolute;inset:0;background:rgba(20,20,20,.55)}
.subscribe{left:235px;top:-46px;width:728px;height:74px;background:var(--white);border-radius:4px;box-shadow:0 3px 12px rgba(0,0,0,.25);z-index:2}
.subscribe h3{position:absolute;left:76px;top:18px;font-size:20px;font-weight:700;color:var(--gold)}
.subscribe small{position:absolute;left:77px;top:43px;font-size:11px;font-weight:600}
.subscribe .email{position:absolute;left:313px;top:25px;width:237px;height:28px;border:1px solid var(--line);border-radius:3px;font-size:9px;font-style:italic;color:#aaa;padding:8px 15px}
.subscribe .send{position:absolute;left:574px;top:25px;width:85px;height:28px;border-radius:4px;background:linear-gradient(90deg,var(--gold),#c0862a 60%,#3a2f22);color:var(--white);font-size:11px;font-weight:700;display:flex;align-items:center;justify-content:center}
.footer-brand{left:212px;top:175px;display:flex;align-items:center;gap:8px;font-size:17px;font-weight:700;color:var(--gold);z-index:1}
.footer-brand i{width:14px;height:14px;background:var(--gold);display:block}
.fcol{top:80px;color:var(--white);z-index:1}
.fcol h5{font-size:14px;font-weight:600;letter-spacing:.4px;margin-bottom:12px}
.fcol li{list-style:none;font-size:11px;height:34.6px;display:flex;align-items:flex-start;gap:5px;white-space:nowrap}
.fcol .circles{display:flex;gap:6px}
.fcol .circles span{width:18px;height:18px;border-radius:50%;background:var(--white);display:block}
.copyright{top:360px;height:51px;background:var(--gold);color:var(--white);font-size:10px;font-weight:600;display:flex;align-items:center;justify-content:center;width:1200px;position:absolute;left:0}
</style>
</head>
<body>

<div class="topbar abs">
  <div class="phone abs">
    <svg width="11" height="11" viewBox="0 0 24 24"><path fill="#fff" d="M6.6 10.8a15 15 0 0 0 6.6 6.6l2.2-2.2a1 1 0 0 1 1-.25 11 11 0 0 0 3.6.57 1 1 0 0 1 1 1V20a1 1 0 0 1-1 1A17 17 0 0 1 3 4a1 1 0 0 1 1-1h3.5a1 1 0 0 1 1 1c0 1.25.2 2.45.57 3.57a1 1 0 0 1-.25 1z"/></svg>
    (555) 010-4832
  </div>
  <div class="socials abs"><span></span><span></span><span></span><span></span></div>
</div>

<header class="site-header">
  <div class="brand abs"><i></i>COBALTRINE</div>
  <div class="apply-btn abs">APPLY FOR A JOB</div>
  <nav class="main-nav abs">
    <a style="left:0">Home</a>
    <a style="left:78px">About Us</a>
    <a style="left:178px">Divisions</a>
    <a style="left:275px">Supplies</a>
    <a style="left:370px">Gallery</a>
    <a style="left:454px">Contact Us</a>
    <svg class="abs" style="left:565px;top:2px" width="12" height="12" viewBox="0 0 24 24"><circle cx="10" cy="10" r="7" fill="none" stroke="#1d1d1d" stroke-width="3"/><path d="M15 15l6 6" stroke="#1d1d1d" stroke-width="3"/></svg>
  </nav>
</header>

<section class="hero">
  <div class="photo" role="img" aria-label="Construction crew silhouetted against a sunset sky beside a crane bucket, with a worker holding a blue hard hat"></div>
  <div class="welcome abs">Welcome To</div>
  <h1 class="abs">COBALTRINE <em>BUILDING</em><br>COMPANY</h1>
  <div class="btn learn abs">LEARN MORE</div>
  <div class="btn contact abs">CONTACT US</div>
  <div class="arrow abs" style="left:22px"><svg width="10" height="12" viewBox="0 0 10 12"><path d="M7 1L2 6l5 5" fill="none" stroke="#1d1d1d" stroke-width="2.4"/></svg></div>
  <div class="arrow abs" style="left:1145px"><svg width="10" height="12" viewBox="0 0 10 12"><path d="M3 1l5 5-5 5" fill="none" stroke="#1d1d1d" stroke-width="2.4"/></svg></div>
</section>

<section class="about">
  <div class="portrait abs" role="img" aria-label="Two businessmen reviewing construction plans on a building site"></div>
  <h2 class="abs">About Us</h2>
  <div class="rule abs"></div>
  <p class="abs">Lorem ipsum proin gravida nibh vel velit auctor aliquet. Aenean sollicitudin, lorem quis bibendum auctor, nisi elit consequat ipsum, nec sagittis sem nibh id elit. Duis sed odio sit amet nibh vulputate cursus a sit amet mauris. Morbi accumsan ipsum velit. Nam nec tellus a odio tincidunt auctor a ornare odio. Sed non mauris vitae erat consequat.</p>
  <div class="read abs">READ MORE</div>
  <div class="years abs">10</div>
  <div class="years-label abs">Years in<br>Business</div>
</section>

<section class="divisions">
  <div class="division abs" style="left:30px">
    <div class="img" role="img" aria-label="Tower cranes over a steel-reinforced concrete structure" style="background:linear-gradient(180deg,#3c5aa0 0%,#6a6e80 40%,#2b2f3a 100%)"></div>
    <h3>Industrial</h3>
    <p>Duis sed odio sit amet nibh vulputate cursus a sit amet mauris. Morbi accumsan ipsum velit. Nam nec tellus.</p>
  </div>
  <div class="division abs" style="left:418px">
    <div class="img" role="img" aria-label="Commercial high-rise under construction with a crane" style="background:linear-gradient(180deg,#1d3f8a 0%,#4d6aa0 40%,#2a2a30 100%)"></div>
    <h3>Commercial</h3>
    <p>Duis sed odio sit amet nibh vulputate cursus a sit amet mauris. Morbi accumsan ipsum velit. Nam nec tellus.</p>
  </div>
  <div class="division abs" style="left:805px">
    <div class="img" role="img" aria-label="Timber frame of a residential house being built" style="background:linear-gradient(180deg,#b9906a 0%,#8b6848 45%,#3a2d25 100%)"></div>
    <h3>Residential</h3>
    <p>Duis sed odio sit amet nibh vulputate cursus a sit amet mauris. Morbi accumsan ipsum velit. Nam nec tellus.</p>
  </div>
</section>

<section class="services">
  <h2 class="section-title abs" style="top:30px">Our Services</h2>
  <div class="title-rule abs" style="top:78px"></div>
  <div class="worker abs" role="img" aria-label="Smiling construction worker in a yellow hard hat with arms crossed"></div>
  <div class="svc left abs" style="top:124px"><h4>DEMOLITION</h4><p>Duis sed odio sit amet nibh vulputate cursus a<br>sit amet mauris. Morbi accums.</p></div>
  <div class="svc left abs" style="top:243px"><h4>GRADING</h4><p>Duis sed odio sit amet nibh vulputate cursus a<br>sit amet mauris. Morbi accums.</p></div>
  <div class="svc left abs" style="top:361px"><h4>CONCRETE SERVICES</h4><p>Duis sed odio sit amet nibh vulputate cursus a<br>sit amet mauris. Morbi accums.</p></div>
  <div class="svc right abs" style="top:124px"><h4>DE-CONSTRUCTION</h4><p>Duis sed odio sit amet nibh vulputate cursus<br>a sit amet mauris. Morbi accums.</p></div>
  <div class="svc right abs" style="top:243px"><h4>EXCAVATION</h4><p>Duis sed odio sit amet nibh vulputate cursus<br>a sit amet mauris. Morbi accums.</p></div>
  <div class="svc right abs" style="top:361px"><h4>CONSTRUCTIONS</h4><p>Duis sed odio sit amet nibh vulputate cursus<br>a sit amet mauris. Morbi accums.</p></div>
</section>

<section class="stats">
  <div class="stat abs" style="left:190px">
    <svg width="30" height="30" viewBox="0 0 30 30"><circle cx="15" cy="9" r="7" fill="#fff"/><path d="M3 29c0-7 5-11 12-11s12 4 12 11z" fill="#fff"/></svg>
    <b>1780</b><span>CLIENT</span>
  </div>
  <div class="stat abs" style="left:395px">
    <svg width="30" height="30" viewBox="0 0 30 30"><rect x="2" y="13" width="6" height="15" fill="#fff"/><path d="M10 13l6-10c2 0 3 2 2 5l-1 4h9c2 0 3 2 2 4l-3 10c-1 2-2 2-3 2H10z" fill="#fff"/></svg>
    <b>1560</b><span>SATISFIED</span>
  </div>
  <div class="stat abs" style="left:603px">
    <svg width="30" height="30" viewBox="0 0 30 30"><rect x="2" y="8" width="26" height="19" rx="2" fill="#fff"/><rect x="10" y="3" width="10" height="6" rx="1" fill="none" stroke="#fff" stroke-width="2"/><rect x="2" y="15" width="26" height="2" fill="#f6a823"/></svg>
    <b>1640</b><span>PROJECTS DONE</span>
  </div>
  <div class="stat abs" style="left:810px">
    <svg width="30" height="30" viewBox="0 0 30 30"><path d="M8 3h14v8a7 7 0 0 1-14 0z" fill="#fff"/><path d="M8 6H3c0 5 2 7 5 7M22 6h5c0 5-2 7-5 7" fill="none" stroke="#fff" stroke-width="2"/><rect x="13" y="18" width="4" height="6" fill="#fff"/><rect x="9" y="24" width="12" height="4" fill="#fff"/></svg>
    <b>1402</b><span>AWARDS</span>
  </div>
</section>

<section class="testimonials">
  <h2 class="section-title abs" style="top:22px">Client Says About Us</h2>
  <div class="title-rule abs" style="top:70px"></div>
  <div class="avatar abs" style="left:78px;top:85px;width:62px;height:62px" role="img" aria-label="Client portrait"></div>
  <div class="avatar abs" style="left:993px;top:96px;width:40px;height:40px" role="img" aria-label="Client portrait"></div>
  <div class="avatar abs" style="left:1136px;top:143px;width:90px;height:90px" role="img" aria-label="Client portrait"></div>
  <div class="avatar abs" style="left:544px;top:101px;width:112px;height:112px;background:linear-gradient(160deg,#888,#333)" role="img" aria-label="Portrait of the quoted client"></div>
  <div class="avatar abs" style="left:118px;top:369px;width:34px;height:34px" role="img" aria-label="Client portrait"></div>
  <div class="avatar abs" style="left:711px;top:360px;width:63px;height:63px" role="img" aria-label="Client portrait"></div>
  <div class="avatar abs" style="left:1028px;top:341px;width:64px;height:64px" role="img" aria-label="Client portrait"></div>
  <p class="quote abs">"Lorem Ipsum is simply dummy text of the printing and typesetting industry. Lorem Ipsum has<br>been the industry's standard dummy text ever since the 1500s."</p>
  <div class="name abs">JOHN DOE</div>
  <div class="role abs">Client</div>
  <div class="dots abs"><i></i><i class="on"></i><i></i></div>
</section>

<section class="why">
  <div class="photo" role="img" aria-label="Yellow excavator digging soil at sunset"></div>
  <div class="disc abs"></div>
  <h2 class="abs">Why Choose Us?</h2>
  <div class="rule abs"></div>
  <p class="abs">Lorem ipsum dolor sit amet, consectetur adipisicing elit, sed do eiusmod tempor incididunt ut labore et dolore magna aliqua. Ut enim ad minim veniam, quis nostrud exercitation ullamco laboris nisi ut aliquip ex ea commodo consequat. Duis aute irure dolor in reprehenderit in voluptate velit esse cillum dolore eu fugiat nulla pariatur. Excepteur sint occaecat.<br><br>cupidatat non proident, sunt in culpa qui officia deserunt mollit anim id est laborum. Sed ut perspiciatis unde omnis iste natus error sit voluptatem accusantium.</p>
  <div class="btn abs">READ MORE</div>
</section>

<section class="contact">
  <h2 class="abs">Contact Us</h2>
  <div class="rule abs"></div>
  <div class="help abs">NEED HELP? CALL US</div>
  <div class="big-phone abs">+(555) 20-4817</div>
  <div class="addr abs">Qirwan Ave 48 Street Masira City KSA.</div>
  <div class="mail abs">info@cobaltrine.test</div>
  <div class="field abs" style="top:70px;height:35px">Name:
    <svg width="14" height="14" viewBox="0 0 24 24"><circle cx="12" cy="7" r="5" fill="#777"/><path d="M2 23c0-6 4-9 10-9s10 3 10 9z" fill="#777"/></svg></div>
  <div class="field abs" style="top:121px;height:35px">Email:
    <svg width="15" height="13" viewBox="0 0 24 18"><rect width="24" height="18" rx="2" fill="#777"/><path d="M1 2l11 8 11-8" fill="none" stroke="#fff" stroke-width="2"/></svg></div>
  <div class="field abs" style="top:171px;height:112px">Message:
    <svg width="16" height="14" viewBox="0 0 24 20"><path d="M2 2h14v9H7l-4 3v-3H2z" fill="#777"/><path d="M18 6h4v9h-1v3l-4-3H9v-2h9z" fill="#777"/></svg></div>
  <div class="submit abs">SUBMIT</div>
</section>

<nav class="footer-nav">
  <a style="left:152px">Home</a>
  <a style="left:231px">About Us</a>
  <a style="left:330px">Divisions</a>
  <a style="left:428px">Supplies</a>
  <a style="left:523px">Gallery</a>
  <a style="left:607px">Contact Us</a>
  <svg class="abs" style="left:718px;top:2px" width="12" height="12" viewBox="0 0 24 24"><circle cx="10" cy="10" r="7" fill="none" stroke="#1d1d1d" stroke-width="3"/><path d="M15 15l6 6" stroke="#1d1d1d" stroke-width="3"/></svg>
</nav>

<footer class="site-footer">
  <div class="photo" role="img" aria-label="Blurred construction worker in a hard hat and high-visibility vest"></div>
  <div class="subscribe abs">
    <h3>SUBSCRIBE</h3>
    <small>OUR NEWSLETTER</small>
    <div class="email">Your Email Address*</div>
    <div class="send">SEND</div>
  </div>
  <div class="footer-brand abs"><i></i>COBALTRINE</div>
  <div class="fcol abs" style="left:392px">
    <h5>SITE MAP</h5>
    <ul><li>› Home</li><li>› About Us</li><li>› Divisions</li><li>› Supplies</li><li>› Gallery</li><li>› Apply For A Job</li></ul>
  </div>
  <div class="fcol abs" style="left:611px">
    <h5>USEFUL LINKS</h5>
    <ul><li>› Terms &amp; Conditions</li><li>› Blogs</li><li>› Privacy Policy</li><li>› Testimonials</li><li>› Partners</li></ul>
  </div>
  <div class="fcol abs" style="left:831px">
    <h5>CONTACT US</h5>
    <ul>
      <li><svg width="9" height="12" viewBox="0 0 10 14"><path d="M5 0a5 5 0 0 1 5 5c0 4-5 9-5 9S0 9 0 5a5 5 0 0 1 5-5z" fill="#fff"/></svg>77 Harith Street, Dunmar,</li>
      <li style="padding-left:20px">Northvale Country</li>
      <li><svg width="10" height="10" viewBox="0 0 24 24"><path d="M6.6 10.8a15 15 0 0 0 6.6 6.6l2.2-2.2a1 1 0 0 1 1-.25 11 11 0 0 0 3.6.57 1 1 0 0 1 1 1V20a1 1 0 0 1-1 1A17 17 0 0 1 3 4a1 1 0 0 1 1-1h3.5a1 1 0 0 1 1 1c0 1.25.2 2.45.57 3.57a1 1 0 0 1-.25 1z" fill="#fff"/></svg>(555) 456-0192</li>
      <li><svg width="11" height="9" viewBox="0 0 24 18"><rect width="24" height="18" rx="2" fill="#fff"/></svg>info@cobaltrine.test</li>
      <li class="circles"><span></span><span></span><span></span><span></span></li>
    </ul>
  </div>
  <div class="copyright">Copyright © Cobaltrine Building Company 2019 | All Rights Reserved.</div>
</footer>

</body>
</html>
```